Lantern Quillhouse Website

Create website for Legal Management Company which specializes in Law Office Spersriinal Management
System implementation & Training
Global presence
Paralegal Services - Remote or In-Office
Legal Research
- Judge Motion Ruling History
- Opposing Counsel Opposition Research - Historical Filings - Pattern identification
Service by Mail - Ex- Parte Notice

Probate -Heir Finder - Asset Location -

```html
<!DOCTYPE html>
<html lang="en">
<head>
<meta charset="utf-8">
<title>Lantern Quillhouse</title>
<link href="https://fonts.googleapis.com/css2?family=Montserrat:wght@400;500;600;700;800&display=swap" rel="stylesheet">
<style>
:root{
  --navy:#0b1a3f;
  --navy-soft:#2a3f63;
  --slate:#2f4a70;
  --orange:#f3a531;
  --orange-deep:#ef9a1f;
  --sky-top:#6f98bb;
  --sky-bottom:#b9d3e6;
  --paper:#f5f5f5;
  --mist:#e6edf4;
  --ink:#1b2233;
  --muted:#4a4f5c;
  --backdrop:#b3b3b3;
  --white:#ffffff;
}
*{margin:0;padding:0;box-sizing:border-box}
html,body{width:1200px;height:2358px;overflow:hidden;background:var(--backdrop);font-family:"Montserrat",sans-serif;color:var(--ink)}
.stage{position:absolute;left:0;top:0;width:1311px;height:2576px;transform:scale(0.91533);transform-origin:0 0}
.page{position:absolute;left:88px;top:88px;width:1134px;height:2400px;background:var(--white);overflow:hidden}
.abs{position:absolute}

/* hero */
.hero{position:absolute;left:0;top:0;width:1134px;height:680px;background:linear-gradient(160deg,var(--sky-top) 0%,#8fb3d0 45%,var(--sky-bottom) 100%)}
.city{position:absolute;left:570px;top:100px;width:564px;height:510px;background:radial-gradient(ellipse at 60% 45%,#3d5d86 0%,#5d7fa6 40%,rgba(150,185,212,0) 75%)}
.brand{position:absolute;left:35px;top:26px;display:flex;align-items:center;gap:12px}
.brand-dot{width:40px;height:40px;border-radius:50%;background:var(--orange)}
.brand-name{font-weight:800;font-size:22px;line-height:24px;color:var(--navy-soft);text-transform:uppercase;letter-spacing:.3px}
.nav{position:absolute;top:24px;left:594px;display:flex;align-items:center;gap:0}
.nav a{font-size:13px;font-weight:500;color:var(--navy);text-decoration:none;padding:0 14px;line-height:28px}
.nav a.active{color:var(--orange);font-weight:600;position:relative}
.nav a.active::after{content:"";position:absolute;left:27px;bottom:1px;width:14px;height:1px;background:var(--orange)}
.nav a.cta{background:var(--orange);margin-left:4px;padding:0 10px}
.hero-title{position:absolute;left:58px;top:197px;font-size:29px;font-weight:800;line-height:41px;color:var(--slate);text-transform:uppercase}
.hero-title .hl{color:var(--orange)}
.hero-sub{position:absolute;left:58px;top:334px;border-left:2px solid var(--orange);padding-left:11px;font-size:13px;line-height:22px;color:var(--white);width:400px}
.btn{display:inline-block;font-weight:700;font-size:12px;text-transform:uppercase;color:var(--white);text-align:center}
.hero-btn{position:absolute;left:58px;top:404px;width:241px;height:34px;line-height:34px;background:var(--orange)}

/* section heads */
.head{position:absolute;left:0;width:1134px;text-align:center;font-weight:800;text-transform:uppercase;color:var(--navy)}
.head .hl{color:var(--orange)}
.rule{position:absolute;height:1px;background:linear-gradient(90deg,rgba(243,165,49,0),var(--orange),rgba(243,165,49,0))}

/* services */
.skyline{position:absolute;left:0;top:960px;width:1134px;height:120px;background:linear-gradient(180deg,rgba(235,237,240,0) 0%,#eceef1 60%)}
.card{position:absolute;top:733px;width:197px;height:310px}
.card-photo{position:absolute;left:0;top:0;width:100%;height:160px}
.card-icon{position:absolute;left:76px;top:849px;width:46px;height:46px;border-radius:50%}
.card-body{position:absolute;left:0;top:160px;width:100%;height:150px;padding:22px 10px 0;text-align:center}
.card h3{font-size:13px;font-weight:700;line-height:17px;margin-bottom:5px}
.card p{font-size:9.6px;line-height:13.4px}
.card.dark .card-body{background:var(--navy)}
.card.dark h3{color:var(--orange)}
.card.dark p{color:var(--white)}
.card.light .card-body{background:var(--orange)}
.card.light h3,.card.light p{color:var(--navy)}

/* about */
.about{position:absolute;left:0;top:1099px;width:1134px;height:433px;background:var(--paper)}
.about-h{position:absolute;left:587px;top:1144px;font-size:30px;font-weight:800;color:var(--navy)}
.about-h .hl{color:var(--orange)}
.about-copy{position:absolute;left:587px;top:1215px;width:390px;font-size:9.8px;line-height:14px;color:var(--muted)}
.about-copy p{margin-bottom:14px}
.learn{position:absolute;left:587px;top:1443px;width:93px;height:26px;line-height:26px;background:var(--navy);font-size:11px}

/* stats */
.stat{position:absolute;top:1562px}
.stat b{display:block;font-size:31px;font-weight:800;color:var(--orange);line-height:34px}
.stat span{display:block;font-size:15px;font-weight:500;letter-spacing:1.4px;color:var(--navy);text-transform:uppercase}
.stat-div{position:absolute;top:1570px;width:1px;height:40px;background:#d9dce2}

/* audience */
.aud{position:absolute;top:1774px;width:200px;text-align:center}
.aud-ring{width:78px;height:78px;margin:0 auto;border-radius:50%;background:var(--white);border:1px solid #d7dbe2;display:flex;align-items:center;justify-content:center}
.aud-label{margin-top:26px;font-size:15px;font-weight:500;letter-spacing:1.5px;color:var(--navy);text-transform:uppercase}
.aud-rule{width:60px;height:1px;margin:6px auto 0;background:linear-gradient(90deg,rgba(243,165,49,0),var(--orange),rgba(243,165,49,0))}

/* contact */
.contact-bg{position:absolute;left:0;top:1900px;width:1134px;height:441px;background:linear-gradient(180deg,#eef2f7,var(--mist))}
.contact-h{position:absolute;left:105px;top:2094px;font-size:29px;font-weight:800;color:var(--slate)}
.contact-h .hl{color:var(--orange)}
.contact-lead{position:absolute;left:105px;top:2144px;font-size:11px;line-height:16px;color:var(--muted)}
.contact-line{position:absolute;left:105px;display:flex;align-items:center;gap:8px;font-size:11.5px;color:var(--navy)}
.contact-line i{width:25px;height:25px;border-radius:50%;border:1px solid var(--orange);display:flex;align-items:center;justify-content:center}
.field{position:absolute;background:var(--white);font-size:9.6px;color:#5a6070;padding:9px 10px}
.send{position:absolute;left:586px;top:2242px;width:125px;height:27px;line-height:27px;background:var(--orange);color:var(--navy);font-size:11px}
.desk{position:absolute;left:740px;top:2030px;width:380px;height:300px;background:radial-gradient(ellipse at 55% 55%,#9fb6cf 0%,#c8d6e5 45%,rgba(230,237,244,0) 75%)}

/* footer */
.footer{position:absolute;left:0;top:2341px;width:1134px;height:59px;background:var(--navy-soft);color:var(--white);text-align:center}
.footer nav{padding-top:10px;font-size:10px}
.footer nav a{color:var(--white);text-decoration:none;margin:0 18px}
.footer small{display:block;margin-top:8px;font-size:9.6px}
</style>
</head>
<body>
<div class="stage">
<div class="page">

  <!-- HERO -->
  <section class="hero">
    <div class="city" role="img" aria-label="Misty blue city skyline of tall glass skyscrapers with faint line icons"></div>
    <div class="brand"><span class="brand-dot"></span><span class="brand-name">Lantern<br>Quillhouse</span></div>
    <nav class="nav">
      <a class="active">Home</a><a>Services</a><a>About</a><a>Blog</a><a>Team</a><a class="cta">Contact</a>
    </nav>
    <h1 class="hero-title"><span class="hl">Comprehensive</span><br>Legal Management<br>&amp; Paralegal Services</h1>
    <p class="hero-sub">Implementing law office systems, providing expert paralegal support and performing in-depth legal research worldwide.</p>
    <a class="btn hero-btn">Schedule a Consultation</a>
  </section>
  <svg class="abs" style="left:0;top:520px" width="1134" height="170" viewBox="0 520 1134 170">
    <polygon points="0,676 567,545 1134,676 1134,690 0,690" fill="#ffffff"/>
    <polygon points="0,648 567,535 567,545 0,676" fill="#2a3f63"/>
    <polygon points="567,535 1134,645 1134,676 567,545" fill="#f3a531"/>
  </svg>

  <!-- SERVICES -->
  <h2 class="head" style="top:624px;font-size:30px;line-height:36px">Our<br><span class="hl">Services</span></h2>
  <div class="rule" style="left:450px;top:710px;width:235px"></div>
  <div class="skyline"></div>

  <article class="card dark" style="left:58px">
    <div class="card-photo" role="img" aria-label="Presenter showing charts on a screen to a team" style="background:linear-gradient(135deg,#c8d3e0,#3f6aa8 60%,#1f2f52)"></div>
    <div class="card-body"><h3>Management System Implementation &amp; Training</h3><p>Deploy custom law office management systems and train your team to streamline operations and ensure compliance.</p></div>
  </article>
  <article class="card light" style="left:263px">
    <div class="card-photo" role="img" aria-label="Paralegals working together beside scales of justice" style="background:linear-gradient(135deg,#e8e2da,#8a7a6a 55%,#2a2d3a)"></div>
    <div class="card-body"><h3>Paralegal<br>Services</h3><p>Certified paralegals available remotely or on-site to assist with document preparation, filings and case management.</p></div>
  </article>
  <article class="card dark" style="left:469px">
    <div class="card-photo" role="img" aria-label="Researcher at a laptop in a law library" style="background:linear-gradient(135deg,#5a3a22,#8c5a30 50%,#1f1b1a)"></div>
    <div class="card-body"><h3>Legal<br>Research</h3><p>Comprehensive research including motion ruling history, opposing counsel research and pattern identification of historical filings.</p></div>
  </article>
  <article class="card light" style="left:674px">
    <div class="card-photo" role="img" aria-label="Laptop showing an incoming mail notice" style="background:linear-gradient(135deg,#d9d5cf,#8c8a88 55%,#2b2b30)"></div>
    <div class="card-body"><h3>Service by<br>Mail</h3><p>Efficient handling of ex-parte notices and legal document service by mail in domestic and international jurisdictions.</p></div>
  </article>
  <article class="card dark" style="left:880px">
    <div class="card-photo" role="img" aria-label="Magnifying glass over a small model house" style="background:linear-gradient(135deg,#c9d1dc,#6f7f93 55%,#3a2a22)"></div>
    <div class="card-body"><h3>Probate &amp; Asset<br>Location</h3><p>Locate heirs and identify assets to simplify probate proceedings and ensure equitable distribution.</p></div>
  </article>
  <span class="card-icon" style="left:134px;top:850px;background:var(--orange)"></span>
  <span class="card-icon" style="left:339px;top:850px;background:var(--navy)"></span>
  <span class="card-icon" style="left:545px;top:850px;background:var(--orange)"></span>
  <span class="card-icon" style="left:750px;top:850px;background:var(--navy)"></span>
  <span class="card-icon" style="left:956px;top:850px;background:var(--orange)"></span>

  <!-- ABOUT -->
  <section class="about"></section>
  <svg class="abs" style="left:0;top:1099px" width="560" height="433">
    <polygon points="0,0 328,0 105,433 0,433" fill="#0b1a3f"/>
    <polygon points="58,51 316,51 192,381 58,381" fill="#f3a531"/>
    <rect x="58.5" y="51.5" width="487" height="330" fill="none" stroke="#f3a531" stroke-width="3"/>
  </svg>
  <div class="abs" role="img" aria-label="Professional woman reading a document beside scales of justice and a gavel" style="left:77px;top:1169px;width:457px;height:293px;background:linear-gradient(120deg,#8a8f96 0%,#c9ccd0 45%,#e8e9ea 70%,#bfc2c5 100%)"></div>
  <h2 class="about-h">ABOUT <span class="hl">US</span></h2>
  <div class="about-copy">
    <p>Lantern Quillhouse is a global legal management company dedicated to empowering law firms with modern systems, expert paralegal support and thorough legal research.</p>
    <p>Our team brings decades of experience in law office operations, technology and procedural compliance. We are committed to professionalism, efficiency and accuracy—helping firms increase productivity and deliver superior outcomes for their clients.</p>
    <p>Lorem ipsum dolor sit amet, consectetuer adipiscing elit, sed diam nonummy nibh euismod tincidunt ut laoreet dolore magna aliquam erat volutpat. Ut wisi enim ad minim veniam, quis nostrud exerci tation ullamcorper suscipit lobortis nisl ut aliquip ex ea commodo consequat. Duis autem vel eum iriure dolor.</p>
  </div>
  <a class="btn learn">Learn More</a>

  <!-- STATS -->
  <div class="stat" style="left:58px"><b>350+</b><span>Family Served</span></div>
  <div class="stat-div" style="left:264px"></div>
  <div class="stat" style="left:326px"><b>450+</b><span>Lawyers Helped</span></div>
  <div class="stat-div" style="left:556px"></div>
  <div class="stat" style="left:617px"><b>#2</b><span>Ranked in NY</span></div>
  <div class="stat-div" style="left:812px"></div>
  <div class="stat" style="left:874px"><b>$2M+</b><span>Earned in Fees</span></div>
  <div class="abs" style="left:0;top:1651px;width:1134px;height:1px;background:#dfe2e7"></div>

  <!-- WHO WE WORK WITH -->
  <h2 class="head" style="top:1696px;font-size:30px">Who We <span class="hl">Work With</span></h2>
  <div class="rule" style="left:430px;top:1746px;width:275px"></div>
  <div class="abs" style="left:0;top:1818px;width:1134px;border-top:1px dotted #d3d7de"></div>

  <div class="aud" style="left:100px">
    <div class="aud-ring"><svg width="40" height="40" viewBox="0 0 40 40" fill="none" stroke="#0b1a3f" stroke-width="1.6"><circle cx="13" cy="9" r="4"/><circle cx="27" cy="9" r="4"/><circle cx="20" cy="20" r="3"/><path d="M7 34V20l6-5 6 5M33 34V20l-6-5-6 5M16 34v-8h8v8"/></svg></div>
    <div class="aud-label">Parents</div><div class="aud-rule"></div>
  </div>
  <div class="aud" style="left:345px">
    <div class="aud-ring"><svg width="40" height="40" viewBox="0 0 40 40" fill="none" stroke="#0b1a3f" stroke-width="1.6"><circle cx="9" cy="14" r="4"/><circle cx="31" cy="14" r="4"/><circle cx="20" cy="22" r="3.5"/><path d="M20 4l2 4 4 .5-3 3 1 4-4-2-4 2 1-4-3-3 4-.5z"/><path d="M12 36v-5a8 8 0 0116 0v5"/></svg></div>
    <div class="aud-label">Entrepreneurs</div><div class="aud-rule"></div>
  </div>
  <div class="aud" style="left:590px">
    <div class="aud-ring"><svg width="40" height="40" viewBox="0 0 40 40" fill="none" stroke="#0b1a3f" stroke-width="1.6"><rect x="12" y="6" width="16" height="16"/><path d="M16 10h2M22 10h2M16 14h2M22 14h2"/><circle cx="20" cy="24" r="4"/><path d="M10 36v-4a10 6 0 0120 0v4"/></svg></div>
    <div class="aud-label">Founders</div><div class="aud-rule"></div>
  </div>
  <div class="aud" style="left:835px">
    <div class="aud-ring"><svg width="40" height="40" viewBox="0 0 40 40" fill="none" stroke="#0b1a3f" stroke-width="1.6"><circle cx="16" cy="13" r="6"/><circle cx="30" cy="10" r="4"/><path d="M5 34v-4a11 8 0 0122 0v4z"/><rect x="24" y="24" width="11" height="10"/></svg></div>
    <div class="aud-label">Business Owner</div><div class="aud-rule"></div>
  </div>

  <!-- CONTACT -->
  <div class="contact-bg"></div>
  <svg class="abs" style="left:0;top:1895px" width="1134" height="170" viewBox="0 1895 1134 170">
    <polygon points="0,1895 1134,1895 1134,1918 567,2058 0,1918" fill="#ffffff"/>
    <polygon points="0,1918 567,2058 0,1945" fill="#2a3f63"/>
    <polygon points="1134,1918 567,2058 1134,1945" fill="#f3a531"/>
  </svg>
  <div class="desk" role="img" aria-label="Isometric laptop with analytics charts, pen holder and floating dashboard cards"></div>

  <h2 class="contact-h">CONTACT <span class="hl">US</span></h2>
  <p class="contact-lead">Ready to transform your legal operations?<br>Reach out for a free consultation.</p>
  <div class="contact-line" style="top:2192px"><i><svg width="13" height="13" viewBox="0 0 14 14" fill="none" stroke="#2a3f63" stroke-width="1.2"><rect x="1" y="3" width="12" height="8"/><path d="M1 3l6 5 6-5"/></svg></i>info@LanternQuillhouse.com</div>
  <div class="contact-line" style="top:2231px"><i><svg width="13" height="13" viewBox="0 0 14 14" fill="none" stroke="#2a3f63" stroke-width="1.2"><path d="M3 1h3l1 3-2 1a7 7 0 004 4l1-2 3 1v3c0 1-1 2-2 2A11 11 0 011 3c0-1 1-2 2-2z"/></svg></i>+1 555 010 2244</div>

  <div class="field" style="left:381px;top:2097px;width:162px;height:28px">Your name</div>
  <div class="field" style="left:549px;top:2097px;width:162px;height:28px">Your phone number</div>
  <div class="field" style="left:381px;top:2132px;width:330px;height:28px">Your email</div>
  <div class="field" style="left:381px;top:2167px;width:330px;height:68px">Your message...</div>
  <a class="btn send">Send Message</a>

  <!-- FOOTER -->
  <footer class="footer">
    <nav><a>HOME</a><a>SERVICES</a><a>ABOUT</a><a>BLOG</a><a>TEAM</a><a>CONTACT</a></nav>
    <small>© 2025 Lantern Quillhouse. All rights reserved.</small>
  </footer>

</div>
</div>
</body>
</html>
```